Data company needs a Website designed, coded and published.

We are a startup data company that needs to build a professional website.
Our business, Quillbrook Analytics, provides PII data to large national advertisers so they can precisely target Real People who are their consumers with advertising messages.

As a startup in this space, our website must establish our credibility and position us against significantly larger and more established competitors. Because we are in a data and technology space, it is vital for this slight to be incredibly slick and professional. Additionally, the purpose of the site is to inform potential customers about the quality of our data, the safety and security measures we take, should provide insight on how a prospect could engage us and ultimately the site should capture potential leads for us.

We have provided the attached presentation deck that is intended to give you an idea of the kind of content we'd like to have on the site. This deck is not intended to restrict your creativity in how the site should look and what it should say. It's simply intended to give you an outline of what we want to say.

We are open to your creative and alternative approaches.

Industry/Entity Type

Technology, Data, Media

Coding

Coded - Design and coding required

Number of Pages Required

5+ page

Font styles to use
Sans Serif

Colors

Designer to choose colors to be used in the design.

Requirements
Must have
• Professional looking site that positions us among the very best in our industry.
Nice to have
• We are about targeting real people with media and so we want to have good clean images of REAL People throughout the site.

```html
<!DOCTYPE html>
<html lang="en">
<head>
<meta charset="utf-8">
<title>Quillbrook Analytics — PII Data for Precise Targeting</title>
<link href="https://fonts.googleapis.com/css2?family=Outfit:wght@400;500;600;700;800&display=swap" rel="stylesheet">
<style>
:root{
  --blue:#1687f5;
  --blue-deep:#0a6fe0;
  --cyan:#12c2f5;
  --ink:#111319;
  --text:#2a2d34;
  --muted:#5b6070;
  --white:#ffffff;
  --dark:#131418;
  --line:#e6e9ef;
}
*{box-sizing:border-box;margin:0;padding:0}
html,body{width:1200px;height:4116px;overflow:hidden}
body{position:relative;background:var(--white);font-family:"Outfit",sans-serif;color:var(--text)}
.abs{position:absolute}
a{color:inherit;text-decoration:none}

/* Header */
.brand{display:flex;align-items:center;gap:10px;font-weight:700;color:var(--ink);font-size:24px}
.brand-dot{width:22px;height:22px;border-radius:50%;background:var(--blue)}
.site-header .brand{left:88px;top:50px}
.main-nav{left:350px;top:32px;display:flex;gap:22px;font-size:15px;font-weight:500;color:var(--ink)}
.btn-demo{left:942px;top:20px;width:168px;height:43px;border:2px solid var(--cyan);border-radius:22px;display:flex;align-items:center;justify-content:center;font-size:15px;font-weight:600;color:var(--ink)}

.btn{display:inline-flex;align-items:center;justify-content:center;height:46px;padding:0 26px;border-radius:23px;font-size:16px;font-weight:600}
.btn-cyan{background:var(--cyan);color:var(--white)}
.btn-white{background:var(--white);color:var(--ink)}

/* Hero */
.hero-title{left:86px;top:296px;font-size:54px;line-height:58px;font-weight:700;color:var(--ink)}
.hero-copy{left:88px;top:428px;width:480px;font-size:18px;line-height:27px;color:var(--text)}
.hero .btn{left:88px;top:502px}
.hex{clip-path:polygon(0 50%,25% 0,75% 0,100% 50%,75% 100%,25% 100%)}
.hero-photo{left:578px;top:130px;width:580px;height:544px;background:linear-gradient(135deg,#24303f,#4a5a6c 55%,#c9b9a4)}

/* Solutions */
.section-title{font-size:46px;font-weight:700;color:var(--ink);text-align:center;width:1200px;left:0}
.solutions-title{top:714px}
.solutions-sub{top:774px;width:1200px;left:0;text-align:center;font-size:18px}
.solutions-row{left:0;top:815px}
.step-label{font-size:19px;font-weight:600;color:var(--ink);text-align:center;width:200px}

/* About */
.about-photo{left:85px;top:1140px;width:485px;height:420px;background:linear-gradient(140deg,#e9eef4,#b8c6d6 50%,#d8b89c);z-index:3}
.about-title{left:613px;top:1236px;font-size:46px;font-weight:700;color:var(--ink)}
.about-copy{left:613px;top:1308px;width:500px;font-size:16px;line-height:24px;color:var(--muted)}
.about .btn{left:611px;top:1442px}

/* Our data band */
.data-band{left:0;top:0;width:1200px;height:2225px}
.data-photo{left:680px;top:1610px;width:520px;height:612px;background:linear-gradient(160deg,rgba(255,255,255,.05),rgba(210,222,236,.45) 45%,rgba(120,140,170,.6));clip-path:polygon(30% 0,70% 0,100% 20%,100% 100%,0 100%,0 60%)}
.data-content{left:88px;top:1700px;width:620px;color:var(--white)}
.data-content .eyebrow{font-size:26px;line-height:30px;font-weight:500;margin:0}
.data-title{font-size:44px;line-height:52px;font-weight:700;margin:6px 0 14px}
.data-content p{font-size:16px;line-height:23px;margin-bottom:10px}
.data-content .btn{margin-top:6px}

/* Service cards */
.service-card{top:2342px;width:470px;height:418px;border-radius:14px;display:flex;align-items:flex-end;justify-content:center;padding-bottom:42px;font-size:28px;font-weight:700;color:var(--white)}
.card-managed{left:122px;background:linear-gradient(160deg,#3c4856,#1f2a35 55%,#31404e)}
.card-data{left:609px;background:linear-gradient(160deg,#5d6a78,#27323d 55%,#141c25)}

/* Campaign reporting */
.dashboard{left:88px;top:2838px;width:509px;height:372px;background:var(--white);border-radius:14px;box-shadow:0 8px 30px rgba(20,30,60,.12)}
.report-title{left:638px;top:2880px;font-size:46px;font-weight:700;color:var(--ink)}
.report-copy{left:643px;top:2956px;width:440px;font-size:16px;line-height:23px;color:var(--muted)}
.report-copy p{margin-bottom:9px}
.slider-dots{left:645px;top:3162px;display:flex;gap:7px}
.slider-dots span{width:9px;height:9px;border-radius:50%;background:#d6dbe3}
.slider-dots span:first-child{background:var(--cyan)}

/* Partners */
.partners{left:120px;top:3318px;width:960px;display:flex;justify-content:space-between;align-items:center}
.partner{display:flex;align-items:center;gap:8px;font-size:22px;font-weight:600;color:#444a55}
.partner i{width:20px;height:20px;border-radius:50%;display:block}

/* CTA & footer */
.footer-shape{left:0;top:0;width:1200px;height:4116px}
.cta{left:207px;top:3455px;width:786px;height:168px;border-radius:84px;background:linear-gradient(90deg,#13b6f3,#22c8f8);overflow:hidden}
.cta-title{left:67px;top:58px;font-size:40px;font-weight:700;color:var(--white)}
.cta-sub{left:68px;top:106px;font-size:16px;color:var(--white)}
.cta .btn{left:597px;top:57px;height:46px;padding:0 26px}

.site-footer{color:var(--white)}
.site-footer .brand{left:85px;top:3880px;color:var(--white);font-size:28px}
.site-footer .brand-dot{background:var(--cyan)}
.footer-col{top:3815px}
.footer-col h4{font-size:22px;font-weight:600;margin-bottom:16px}
.footer-col li{list-style:none;font-size:13px;line-height:24px;color:#d8dbe1}
.col-links{left:407px}
.col-news{left:616px}
.col-contact{left:882px}
.newsletter-field{margin-top:14px;width:216px;height:40px;border-radius:20px;background:#2a2c33;display:flex;align-items:center;justify-content:space-between;padding:0 16px 0 22px;font-size:13px}
.contact-row{display:flex;align-items:center;gap:10px}
.social{display:flex;gap:12px;margin-top:10px;font-size:12px;font-weight:600;color:var(--white)}
.footer-rule{left:88px;top:4060px;width:1024px;height:1px;background:#2f3139}
.copyright{left:0;width:1200px;top:4080px;text-align:center;font-size:12px;color:#d8dbe1}
.to-top{left:1124px;top:4050px;width:32px;height:36px;background:var(--blue);clip-path:polygon(50% 0,100% 25%,100% 75%,50% 100%,0 75%,0 25%)}
</style>
</head>
<body>

<svg class="abs data-band" viewBox="0 0 1200 2225" aria-hidden="true">
  <defs>
    <linearGradient id="bandGrad" x1="0" y1="0" x2="1" y2="1">
      <stop offset="0" stop-color="#1b8ff7"/>
      <stop offset="1" stop-color="#0d72e6"/>
    </linearGradient>
  </defs>
  <path d="M0 1560 C30 1470 150 1425 300 1430 L1200 1805 L1200 2222 L0 2222 Z" fill="url(#bandGrad)"/>
</svg>

<svg class="abs footer-shape" viewBox="0 0 1200 4116" aria-hidden="true">
  <path d="M0 3730 L900 3640 C1000 3545 1110 3505 1200 3525 L1200 4116 L0 4116 Z" fill="#131418"/>
</svg>

<header class="site-header">
  <a class="abs brand" href="#"><span class="brand-dot"></span>Quillbrook Analytics</a>
  <nav class="abs main-nav">
    <a href="#">Our Data</a><a href="#">Solutions</a><a href="#">About Us</a><a href="#">Why Quillbrook?</a><a href="#">Careers</a><a href="#">Contact</a>
  </nav>
  <a class="abs btn-demo" href="#">Schedule a Demo</a>
</header>

<section class="hero">
  <h1 class="abs hero-title">PII Data for<br>Precise Targeting</h1>
  <p class="abs hero-copy">Ethically and intelligently target REAL PEOPLE with your programmatic media. No Cookies. No Bots.</p>
  <a class="abs btn btn-cyan" href="#">Learn More</a>
  <div class="abs hero-photo hex" role="img" aria-label="Photo of two analysts reviewing data on a large wall display"></div>
</section>

<section class="solutions">
  <h2 class="abs section-title solutions-title">Solutions</h2>
  <p class="abs solutions-sub">Three Steps to Drive Results</p>
  <svg class="abs solutions-row" width="1200" height="260" viewBox="0 0 1200 260" aria-hidden="true">
    <defs>
      <filter id="soft" x="-20%" y="-20%" width="140%" height="150%">
        <feDropShadow dx="0" dy="10" stdDeviation="12" flood-color="#1c2a4a" flood-opacity=".1"/>
      </filter>
    </defs>
    <g fill="#ffffff" filter="url(#soft)">
      <polygon points="205,130 268,18 402,18 465,130 402,240 268,240"/>
      <polygon points="470,130 533,18 667,18 730,130 667,240 533,240"/>
      <polygon points="738,130 801,18 935,18 998,130 935,240 801,240"/>
    </g>
    <g fill="none" stroke="#12c2f5" stroke-width="1.6" stroke-dasharray="5 5">
      <path d="M205 130 L268 12 L402 12 L470 130"/>
      <path d="M470 130 L533 8 L667 8 L738 130"/>
      <path d="M738 130 L801 12 L935 12 L1002 138"/>
    </g>
    <path d="M996 132 l6 8 l3 -9" fill="none" stroke="#12c2f5" stroke-width="1.6"/>
    <g font-family="Outfit, sans-serif" font-size="13" font-weight="600" fill="#fff" text-anchor="middle">
      <circle cx="202" cy="130" r="12" fill="#1687f5"/><text x="202" y="135">1</text>
      <circle cx="466" cy="130" r="12" fill="#1687f5"/><text x="466" y="135">2</text>
      <circle cx="734" cy="130" r="12" fill="#12c2f5"/><text x="734" y="135">3</text>
    </g>
    <g fill="none" stroke="#1687f5" stroke-width="2.4">
      <circle cx="318" cy="92" r="9"/><circle cx="336" cy="92" r="9"/><circle cx="354" cy="92" r="9"/>
      <circle cx="327" cy="114" r="8"/><circle cx="345" cy="114" r="8"/>
      <path d="M296 150 q0 -22 20 -22 q16 0 18 22 M316 150 q2 -22 18 -22 q18 0 20 22 M336 150 q2 -22 18 -22 q20 0 20 22"/>
    </g>
    <g fill="none" stroke="#1687f5" stroke-width="2.4">
      <circle cx="603" cy="98" r="14"/>
      <circle cx="603" cy="98" r="24" stroke-dasharray="4 5"/>
      <path d="M598 108 v26 l-8 -6 m8 16 h18 l4 -22 l-14 -3 v-11"/>
      <circle cx="573" cy="82" r="3"/><circle cx="633" cy="82" r="3"/><circle cx="603" cy="68" r="3"/>
    </g>
    <g fill="none" stroke="#1687f5" stroke-width="2.4">
      <rect x="836" y="76" width="34" height="24" rx="2"/>
      <rect x="878" y="74" width="22" height="14" rx="2"/>
      <rect x="878" y="94" width="22" height="14" rx="2"/>
      <rect x="878" y="114" width="22" height="14" rx="2"/>
      <rect x="878" y="134" width="22" height="14" rx="2"/>
      <path d="M840 146 v-16 m-5 5 l5 -5 l5 5 M856 146 v-20 m-5 5 l5 -5 l5 5 M870 146 v-12"/>
    </g>
  </svg>
  <p class="abs step-label" style="left:235px;top:998px">Audience</p>
  <p class="abs step-label" style="left:503px;top:998px">Activation</p>
  <p class="abs step-label" style="left:764px;top:998px">Attribution</p>
</section>

<section class="about">
  <div class="abs about-photo hex" role="img" aria-label="Photo of an analyst reviewing printed charts beside data monitors"></div>
  <h2 class="abs about-title">About Quillbrook</h2>
  <p class="abs about-copy">Quillbrook Analytics allows you to identify the consumers who are just starting their journey...<br>And because we start with the names of Real People...<br>Quillbrook Analytics allows you to track and manage your communication and messaging throughout the entire journey.</p>
  <a class="abs btn btn-cyan" href="#">Learn More</a>
</section>

<section class="our-data">
  <div class="abs data-photo" role="img" aria-label="Photo of a smiling professional holding an open laptop"></div>
  <div class="abs data-content">
    <p class="eyebrow">OUR DATA</p>
    <h2 class="data-title">Quillbrook links Consumer<br>Attributes at the Human Level</h2>
    <p>The rest of the market identifies individuals at the persona level. Some studies show that Personas/Cookies are only 42% accurate!</p>
    <p>Quillbrook Analytics unites both email and physical addresses with actual digital, mobile and offline behavior...all tied back to Real People.</p>
    <p>Leverage our audience data to maintain the integrity of yours.</p>
    <p>Our PII data is 100% secure, permissioned-based, opt-in, and CCPA, GDPR &amp; CAN-SPAM compliant. In addition, we have complete ownership of our data.</p>
    <a class="btn btn-white" href="#">Learn More</a>
  </div>
</section>

<section class="services">
  <a class="abs service-card card-managed" href="#" role="img" aria-label="Photo of a hand holding a tablet with a network platform diagram">Managed Services</a>
  <a class="abs service-card card-data" href="#" role="img" aria-label="Photo of two engineers working with a laptop in a server room">Data Services</a>
</section>

<section class="reporting">
  <svg class="abs dashboard" viewBox="0 0 509 372" aria-label="Campaign dashboard with metric tiles, line charts and bar charts" role="img">
    <circle cx="26" cy="24" r="5" fill="#f5b324"/><circle cx="41" cy="24" r="5" fill="#f1524b"/><circle cx="56" cy="24" r="5" fill="#f78c3c"/>
    <rect x="18" y="46" width="473" height="3" fill="#6a4ec8"/>
    <g font-family="Outfit, sans-serif" fill="#333">
      <text x="20" y="62" font-size="9" font-weight="600">Display</text>
      <text x="78" y="62" font-size="6">Data updated weekly</text>
    </g>
    <g fill="#dfe3f7">
      <rect x="20" y="70" width="34" height="20"/><rect x="62" y="70" width="34" height="20"/><rect x="104" y="70" width="34" height="20"/>
      <rect x="146" y="70" width="34" height="20"/><rect x="188" y="70" width="34" height="20"/><rect x="230" y="70" width="34" height="20"/>
      <rect x="272" y="70" width="34" height="20"/><rect x="314" y="70" width="34" height="20"/><rect x="356" y="70" width="34" height="20"/>
    </g>
    <g fill="#1687f5"><rect x="230" y="70" width="34" height="20" opacity=".3"/><rect x="272" y="70" width="34" height="20" opacity=".3"/></g>
    <g font-family="Outfit, sans-serif" font-size="8" font-weight="600" fill="#222">
      <text x="20" y="112">Leads</text><text x="192" y="106">CPL by Week</text><text x="350" y="106">Visits by Day</text>
      <text x="20" y="250">Ad Size</text><text x="266" y="250">Device</text>
      <text x="20" y="335">Landing Page</text><text x="266" y="335">Creative</text>
    </g>
    <g stroke="#e3e6ee" stroke-width="1">
      <path d="M30 125 H160 M30 165 H160 M30 205 H160 M30 230 H160"/>
      <path d="M190 125 H320 M190 165 H320 M190 205 H320 M190 230 H320"/>
      <path d="M345 125 H480 M345 165 H480 M345 205 H480 M345 230 H480"/>
    </g>
    <path d="M50 225 L100 160" stroke="#334" stroke-width="1.2" fill="none"/>
    <path d="M206 128 L246 220" stroke="#2b6cf0" stroke-width="1.4" fill="none"/>
    <path d="M360 140 L410 150 L460 168" stroke="#2b6cf0" stroke-width="1.2" fill="none"/>
    <path d="M360 146 L410 158 L460 172" stroke="#d0564b" stroke-width="1.2" fill="none"/>
    <g fill="#7b3fd0">
      <rect x="70" y="270" width="28" height="45"/><rect x="106" y="290" width="28" height="25"/><rect x="142" y="300" width="28" height="15"/><rect x="178" y="308" width="28" height="7"/>
      <rect x="306" y="280" width="28" height="35"/><rect x="346" y="305" width="28" height="10"/><rect x="386" y="311" width="28" height="4"/>
    </g>
    <path d="M30 315 H230 M270 315 H480" stroke="#c7cbd6"/>
  </svg>
  <h2 class="abs report-title">Campaign Reporting</h2>
  <div class="abs report-copy">
    <p>Accessible Campaign Customized Dashboard Metrics Provide Guidanceon Day to Day activity.</p>
    <p>These reports help inform mid campaign optimizations and changes.</p>
    <p>However, they are only a snapshot of our progress.</p>
    <p>They do not tell the complete story about the impact to the entire funnel and Lifetime Value.</p>
  </div>
  <div class="abs slider-dots"><span></span><span></span><span></span></div>
</section>

<section class="abs partners" aria-label="Partners">
  <span class="partner"><i style="background:#f07a2a"></i>Northpine</span>
  <span class="partner"><i style="background:#e0357a"></i>Mediaridge</span>
  <span class="partner"><i style="background:#1d8fd8"></i>Velloway</span>
  <span class="partner">Cordalis</span>
  <span class="partner"><i style="background:#f08a32"></i>Brightfen</span>
</section>

<section class="abs cta">
  <h2 class="abs cta-title">Ready to Learn More?</h2>
  <p class="abs cta-sub">Talk to our experts now.</p>
  <a class="abs btn btn-white" href="#">Contact Us</a>
</section>

<footer class="site-footer">
  <a class="abs brand" href="#"><span class="brand-dot"></span>Quillbrook<br>Analytics</a>
  <div class="abs footer-col col-links">
    <h4>Useful Links</h4>
    <ul><li>Our Data</li><li>Solutions</li><li>About Us</li><li>Why Quillbrook?</li><li>Careers</li><li>Contact Us</li></ul>
  </div>
  <div class="abs footer-col col-news">
    <h4>Newsletter</h4>
    <ul><li>Subscribe to pour newsletter</li></ul>
    <div class="newsletter-field">Email Address
      <svg width="14" height="14" viewBox="0 0 14 14" aria-hidden="true"><path d="M1 7 L13 1 L9 13 L7 8 Z" fill="#12c2f5"/></svg>
    </div>
  </div>
  <div class="abs footer-col col-contact">
    <h4>Contact Us</h4>
    <ul>
      <li class="contact-row"><svg width="10" height="13" viewBox="0 0 10 13" aria-hidden="true"><path d="M5 0 C2 0 0 2 0 5 C0 8 5 13 5 13 C5 13 10 8 10 5 C10 2 8 0 5 0 Z" fill="#12c2f5"/></svg>Some goes address here</li>
      <li class="contact-row"><svg width="12" height="9" viewBox="0 0 12 9" aria-hidden="true"><rect width="12" height="9" rx="1" fill="#12c2f5"/><path d="M0 1 L6 5 L12 1" stroke="#131418" fill="none"/></svg>info@quillbrook.example</li>
      <li class="contact-row"><svg width="12" height="12" viewBox="0 0 12 12" aria-hidden="true"><path d="M2 0 L4.5 0 L5 3.5 L3.5 4.5 C4.5 6.5 5.5 7.5 7.5 8.5 L8.5 7 L12 7.5 L12 10 C12 11 11 12 10 12 C4.5 12 0 7.5 0 2 C0 1 1 0 2 0 Z" fill="#12c2f5"/></svg>+1 555 010 2040</li>
    </ul>
    <div class="social"><a href="#">Pebl</a><a href="#">Twine</a><a href="#">Orbit</a><a href="#">Nook</a></div>
  </div>
  <div class="abs footer-rule"></div>
  <p class="abs copyright">©Copyright Quillbrook 2023 | All Rights Reserved</p>
  <a class="abs to-top" href="#" aria-label="Back to top"></a>
</footer>

</body>
</html>
```